Business Card Design

Rubber roller servicing company. Specializing in rubber to metal bonding. Serving various industries including, pharmaceutical, textile, plastic extrusion, polythene bag converting, laminating and the food industries.

Industry/Entity Type

Plastic

Contact Information for Business Card

Carwick Roller & Rubber Co Ltd, Trevor Ambleside, Managing Director, Unit at Fernholt, Ridley Lane, Oxenby, Huddersfield, West Yorkshire, HX4 9TJ, Tel 01632 960481, Fax 01632 960527, email info@carwickroller.example.co.uk,

```html
<!DOCTYPE html>
<html lang="en">
<head>
<meta charset="utf-8">
<title>Carwick Roller &amp; Rubber Co Ltd – Business Card</title>
<link rel="stylesheet" href="https://fonts.googleapis.com/css2?family=Lato:wght@400;700;900&family=Didact+Gothic&display=swap">
<style>
  :root {
    --bg: #2a2a2c;
    --card: #ffffff;
    --card-shade: #ececec;
    --ink: #141414;
    --orange: #d9770f;
    --orange-deep: #b8600a;
    --roller-grey: #9c9c9c;
    --roller-red: #c9503a;
  }
  * { box-sizing: border-box; margin: 0; padding: 0; }
  html, body { width: 1200px; height: 900px; overflow: hidden; }
  body {
    background: var(--bg);
    display: flex; align-items: center; justify-content: center;
    font-family: "Didact Gothic", "Lato", sans-serif;
    color: var(--ink);
  }
  .card {
    position: relative;
    width: 1000px; height: 570px;
    background: linear-gradient(135deg, var(--card) 0%, var(--card) 55%, var(--card-shade) 100%);
    overflow: hidden;
  }
  .brand {
    position: absolute; left: 60px; top: 150px;
    display: flex; align-items: center; gap: 12px;
    font-family: "Lato", sans-serif; font-weight: 900;
    font-size: 40px; letter-spacing: 2px; color: var(--ink);
  }
  .brand-mark { width: 22px; height: 22px; background: var(--orange); }
  .product-visual {
    position: absolute; left: 60px; top: 230px;
    width: 400px; height: 230px; border-radius: 18px;
    background: linear-gradient(160deg, var(--roller-red) 0%, #8a8a8a 45%, var(--roller-grey) 75%, #e4e1da 100%);
    opacity: .85;
  }
  .divider {
    position: absolute; left: 515px; top: 150px;
    width: 4px; height: 300px;
    background: linear-gradient(to bottom, rgba(217,119,15,0), var(--orange) 30%);
  }
  .person { position: absolute; right: 70px; top: 55px; text-align: right; }
  .person-name {
    font-family: "Lato", sans-serif; font-weight: 900;
    font-size: 34px; letter-spacing: .5px; text-transform: uppercase;
  }
  .person-role {
    font-family: "Lato", sans-serif; font-weight: 400;
    font-size: 21px; color: var(--orange); margin-top: -2px;
  }
  .contacts {
    position: absolute; left: 550px; top: 160px;
    list-style: none; display: flex; flex-direction: column; gap: 18px;
  }
  .contact { display: flex; align-items: flex-start; gap: 18px; font-size: 21px; line-height: 1.3; }
  .contact svg { width: 34px; height: 30px; flex: none; fill: var(--ink); }
  .company-band {
    position: absolute; right: 0; bottom: 65px; width: 300px; height: 30px;
  }
  .company-name {
    position: absolute; left: 300px; bottom: 28px;
    font-family: "Lato", sans-serif; font-weight: 900;
    font-size: 34px; color: var(--orange); text-transform: uppercase;
  }
</style>
</head>
<body>
  <main class="card">
    <div class="brand"><span class="brand-mark"></span>CARWICKROLLER</div>
    <div class="product-visual" role="img" aria-label="Photograph of assorted rubber-covered industrial rollers"></div>
    <div class="divider"></div>

    <header class="person">
      <h1 class="person-name">Trevor Ambleside</h1>
      <p class="person-role">Managing Director</p>
    </header>

    <ul class="contacts">
      <li class="contact">
        <svg viewBox="0 0 34 30" aria-hidden="true"><path d="M2 9c0-4 6-6 15-6s15 2 15 6v3h-7V9c-2-1-14-1-16 0v3H2z"/><path d="M7 13h20l4 15H3z"/><circle cx="17" cy="20" r="4" fill="#fff"/></svg>
        <span>01632 960481</span>
      </li>
      <li class="contact">
        <svg viewBox="0 0 34 30" aria-hidden="true"><rect x="9" y="2" width="16" height="8"/><rect x="2" y="11" width="30" height="11" rx="2"/><rect x="9" y="18" width="16" height="10" fill="#fff" stroke="#141414" stroke-width="2"/></svg>
        <span>01632 960527</span>
      </li>
      <li class="contact">
        <svg viewBox="0 0 34 30" aria-hidden="true"><path d="M2 5h30v20H2z"/><path d="M2 5l15 12L32 5" fill="none" stroke="#fff" stroke-width="2"/></svg>
        <span>info@carwickroller.example.co.uk</span>
      </li>
      <li class="contact">
        <svg viewBox="0 0 34 30" aria-hidden="true"><path d="M17 1a10 10 0 0 0-10 10c0 8 10 18 10 18s10-10 10-18A10 10 0 0 0 17 1z"/><circle cx="17" cy="11" r="4" fill="#fff"/></svg>
        <span>The Unit at Fernholt, Ridley Lane,<br>Oxenby, Huddersfield,<br>West Yorkshire, HX4 9TJ</span>
      </li>
    </ul>

    <svg class="company-band" viewBox="0 0 300 30" preserveAspectRatio="none" aria-hidden="true">
      <path d="M30 0H300V30H0C12 30 14 0 30 0z" fill="var(--orange)"/>
    </svg>
    <p class="company-name">Carwick Roller &amp; Rubber Co Ltd</p>
  </main>
</body>
</html>
```